Tervolan Pty Ltd professional business card

A professional business card template using the colours from the supplied logo.
Clean crisp lines while, Modern while not being over the top.

Target Market(s)

Construction, commerical and industrial

Industry/Entity Type

Communications

Contact Information for Business Card

For a Communications, IT, Optical fibre installation company

Colors
37b8a4

```html
<!DOCTYPE html>
<html lang="en">
<head>
<meta charset="utf-8">
<title>Tervolan Pty Ltd – Business Card</title>
<link href="https://fonts.googleapis.com/css2?family=Oswald:wght@400;500&display=swap" rel="stylesheet">
<style>
  :root {
    --teal: #1592a3;
    --grey: #6d6e71;
    --white: #ffffff;
    --backdrop: #e4e4e4;
  }
  html, body {
    margin: 0;
    padding: 0;
    width: 1200px;
    height: 1200px;
    overflow: hidden;
    background: var(--backdrop);
  }
  .canvas {
    position: relative;
    width: 1200px;
    height: 1200px;
  }
  .card {
    position: absolute;
    left: 252px;
    width: 696px;
    height: 398px;
    display: block;
  }
  .card--front { top: 163px; }
  .card--back  { top: 639px; }
  .wordmark {
    font-family: "Oswald", sans-serif;
    font-weight: 500;
    font-size: 150px;
    letter-spacing: 4px;
  }
  .wordmark--light { fill: var(--white); }
  .wordmark--grey  { fill: var(--grey); }
  .fill-teal  { fill: var(--teal); }
  .fill-white { fill: var(--white); }
  .contact-text {
    font-family: "Oswald", sans-serif;
    font-weight: 500;
    fill: var(--white);
  }
  .contact-name     { font-size: 54px; }
  .contact-position { font-size: 30px; font-weight: 400; }
  .contact-line     { font-size: 46px; }
  .icon { fill: var(--white); }
  .icon-stroke { fill: none; stroke: var(--white); stroke-width: 3; }
</style>
</head>
<body>
<main class="canvas">

  <!-- Front of card -->
  <svg class="card card--front" viewBox="0 0 1120 640" role="img" aria-label="Tervolan card front">
    <rect class="fill-teal" x="0" y="0" width="1120" height="640" rx="40"/>
    <text class="wordmark wordmark--light" x="560" y="427" text-anchor="middle">TERVOLAN</text>
  </svg>

  <!-- Back of card -->
  <svg class="card card--back" viewBox="0 0 1120 640" role="img" aria-label="Tervolan card back with contact details">
    <defs>
      <clipPath id="card-shape">
        <rect x="0" y="0" width="1120" height="640" rx="40"/>
      </clipPath>
    </defs>
    <g clip-path="url(#card-shape)">
      <rect class="fill-white" x="0" y="0" width="1120" height="640"/>
      <path class="fill-teal" d="M0 290 H560 C800 290 1000 330 1120 388 V402 C1000 344 800 304 560 304 H0 Z"/>
      <path class="fill-teal" d="M0 312 H560 C800 312 1000 353 1120 412 V640 H0 Z"/>
    </g>

    <text class="wordmark wordmark--grey" x="560" y="230" text-anchor="middle">TERVOLAN</text>

    <text class="contact-text contact-name" x="65" y="380">YOUR NAME HERE</text>
    <text class="contact-text contact-position" x="69" y="410">NAME POTITION</text>

    <!-- phone -->
    <path class="icon" d="M66 462 c4-3 8-2 10 2 l4 8 c1 3 0 5-2 7 l-3 2 c2 5 6 9 11 11 l2-3 c2-2 4-3 7-2 l8 4 c4 2 5 6 2 10 l-3 3 c-6 5-18 1-28-9 c-10-10-14-22-9-28 z"/>
    <text class="contact-text contact-line" x="138" y="497">YOUR PHONE</text>

    <!-- email -->
    <rect class="icon-stroke" x="62" y="532" width="30" height="20"/>
    <polyline class="icon-stroke" points="62,532 77,544 92,532"/>
    <text class="contact-text contact-line" x="138" y="560">YOUR EMAIL</text>

    <!-- location -->
    <path class="icon" d="M722 460 c-9 0-15 7-15 15 c0 10 15 25 15 25 c0 0 15-15 15-25 c0-8-6-15-15-15 z M722 469 a6 6 0 1 1 0 12 a6 6 0 1 1 0-12 z" fill-rule="evenodd"/>
    <text class="contact-text contact-line" x="784" y="497">YOUR LOCATION</text>

    <!-- web -->
    <circle class="icon-stroke" cx="722" cy="542" r="12"/>
    <ellipse class="icon-stroke" cx="722" cy="542" rx="5" ry="12"/>
    <line class="icon-stroke" x1="710" y1="542" x2="734" y2="542"/>
    <text class="contact-text contact-line" x="784" y="560">YOUR WEB</text>
  </svg>

</main>
</body>
</html>
```